Home inspection business! professional look attracting customers just by looks. Read must haves

its a new business I started on my own for home inspections I would like something very professional to give to real estate agents and clients, its going to have my license number on it my business phone number my name my website as well etc on the back side it will be servicing areas and also what kind of services I offer I also have a business card from someone else the way I would like mine to be. I will attach my logo

Home Inspection

listed in nice to haves

• phone number - 555 293 8471
• website- hollowpinecheck.com
• license number #2938475610
• my name Gavin keropulis
• picture of my logo and me on the front
• on the back of the card. stating I am servicing All of New York and Long Island
• also services I will offer will be home inspection -mold inspection -lead inspection -radon inspection -Termite Inspection -Infared Scan.
• and also we provide inspections for single family homes condos co-ops town-homes
• and commercial property
• same colors as the logos and also if you recommend fonts to look like the logo not sure up to you

```html
<!DOCTYPE html>
<html lang="en">
<head>
<meta charset="utf-8">
<title>Hollow Pine Home Inspectors – Business Card</title>
<link href="https://fonts.googleapis.com/css2?family=Open+Sans:wght@400;600;700&display=swap" rel="stylesheet">
<style>
  :root {
    --backdrop: #6b6b6b;
    --card: #2a2a2a;
    --blue: #4a95d0;
    --grey: #7d7d7d;
    --text: #f2f2f2;
    --divider: #6f6f6f;
  }
  * { box-sizing: border-box; margin: 0; padding: 0; }
  html, body {
    width: 1200px; height: 1021px; overflow: hidden;
    background: var(--backdrop);
    font-family: "Open Sans", Arial, sans-serif;
    color: var(--text);
  }
  .card {
    position: absolute; left: 220px;
    width: 760px; height: 434px;
    background: var(--card);
    box-shadow: 0 14px 30px rgba(0,0,0,.35);
    overflow: hidden;
  }
  .card--back { top: 48px; }
  .card--front { top: 540px; }

  /* back side */
  .service-area {
    position: absolute; left: 64px; top: 52px;
    font-size: 17px; letter-spacing: .3px; text-transform: uppercase;
  }
  .services {
    position: absolute; left: 78px; top: 96px;
    list-style: none; font-size: 19px; line-height: 27px;
  }
  .services li { position: relative; padding-left: 16px; }
  .services li::before {
    content: ""; position: absolute; left: 0; top: 11px;
    width: 7px; height: 7px; border-radius: 50%; background: var(--blue);
  }
  .property-types {
    position: absolute; left: 64px; top: 300px;
    font-size: 19px; letter-spacing: .2px;
  }
  .accent-stripe {
    position: absolute; left: 440px; top: 374px;
    width: 320px; height: 8px; background: var(--blue);
  }
  .brand-mark {
    position: absolute; right: 48px; top: 150px;
    display: flex; align-items: center; gap: 14px;
    font-size: 26px; font-weight: 700; color: var(--grey);
  }
  .brand-mark .dot {
    width: 22px; height: 22px; border-radius: 50%; background: var(--blue);
  }

  /* front side */
  .logo {
    position: absolute; left: 58px; top: 160px; width: 300px;
    display: flex; align-items: center; gap: 12px;
    font-size: 24px; font-weight: 700; color: var(--grey); line-height: 1.15;
  }
  .logo .dot {
    flex: none; width: 20px; height: 20px; border-radius: 50%; background: var(--blue);
  }
  .divider {
    position: absolute; left: 392px; top: 104px;
    width: 2px; height: 226px; background: var(--divider);
  }
  .contact { position: absolute; left: 432px; top: 112px; }
  .contact__name { font-size: 30px; font-weight: 600; color: var(--blue); line-height: 1.1; }
  .contact__role { font-size: 22px; margin-top: 2px; }
  .contact__lines { margin-top: 30px; font-size: 22px; line-height: 32px; }
  .contact__line { display: flex; align-items: center; gap: 10px; }
  .contact__line svg { width: 20px; height: 20px; flex: none; }
  .license-label { color: var(--blue); }
</style>
</head>
<body>

<section class="card card--back" aria-label="Card back">
  <p class="service-area">All of New York and Long Island</p>
  <ul class="services">
    <li>Home Inspection</li>
    <li>Mold Inspection</li>
    <li>Lead Inspection</li>
    <li>Radon Inspection</li>
    <li>Termite Inspection</li>
    <li>Infared Scan</li>
  </ul>
  <div class="brand-mark"><span class="dot"></span>Hollow Pine</div>
  <p class="property-types">Single Family Homes Condos Co-ops Town-homes • Commercial Property</p>
  <div class="accent-stripe"></div>
</section>

<section class="card card--front" aria-label="Card front">
  <div class="logo"><span class="dot"></span>Hollow Pine Home Inspectors</div>
  <div class="divider"></div>
  <div class="contact">
    <p class="contact__name">Gavin Keropulis</p>
    <p class="contact__role">President</p>
    <div class="contact__lines">
      <p class="contact__line">
        <svg viewBox="0 0 24 24" aria-hidden="true"><path fill="#4a95d0" d="M6.6 10.8a15 15 0 0 0 6.6 6.6l2.2-2.2c.3-.3.7-.4 1-.2 1.1.4 2.3.6 3.6.6.6 0 1 .4 1 1V20c0 .6-.4 1-1 1A17 17 0 0 1 3 4c0-.6.4-1 1-1h3.5c.6 0 1 .4 1 1 0 1.3.2 2.5.6 3.6.1.3 0 .7-.2 1z"/></svg>
        555 293 8471
      </p>
      <p class="contact__line">
        <svg viewBox="0 0 24 24" aria-hidden="true" fill="none" stroke="#4a95d0" stroke-width="2"><circle cx="12" cy="12" r="9"/><path d="M3 12h18M12 3c3 3 3 15 0 18M12 3c-3 3-3 15 0 18"/></svg>
        hollowpinecheck.com
      </p>
      <p class="contact__line"><span class="license-label">License</span> #2938475610</p>
    </div>
  </div>
</section>

</body>
</html>
```